Upcoming Sports Event Banner Ads Design

We need a ad design for an upcoming sporting championship that we will use on several platforms. Unfortunately I have to be discreet in terms of that the event actually is as well as the specifics in terms of logos and what not.

We need the following sizes:

728x90
980x50
300x250
300x525
1000x200

Here is some of what we are trying to promote for the event:

Spring Frenzy - the tag line Spring Frenzy Starts Now can be used

Ticket Pricing
Session tickets are $15. Each session consists of two games, with the exception of the Championship Games on Sunday, March 12. Kid Tickets are $5 per session and include a hot dog and drink.

A button graphic inside the ad can be used as a call out to click here for tickets or just Click Here...you get the idea.

Field Jubilee
Location for this can be just generic
9:00 AM - 12:00 PM

Field Jubilee will include our annual Hoop Hustle event at 11:00 AM, where children ages 3-12 receive a free t-shirt, free basketball, and two free tickets to the men’s semi-final games

It's easier to use more than one of each size for this since the info is spread about - or using animated GIFs.

Looking forward to see what comes out.

Background is going to be uploaded - usage of this is key, doesn't have to be all of it but does need to be incorporated.

Please have an area where a circular logo can fit along with a shield logo - options for both.

Target Market(s)

Sports fans, kids, moms with kids, it's for a sporting event tournament - think GWBA or UCLB Hoopball Invitational, GLF Postseason...that sort of event - just not as big.

Industry/Entity Type

Event

Font styles to use
Other font styles liked:
• DINPro

Requirements
Must have
• Keep font generic - we have our own font that we have to use.
Nice to have
• Multiple options for each design. Or animated GIFs that can be easily edited.
• THis project is more of like a templating since I cannot give out our logos or event information at this time.
Should not have
• Too much text.

```html
<!DOCTYPE html>
<html lang="en">
<head>
<meta charset="utf-8">
<title>Spring Frenzy – 1000x200 Banner</title>
<link href="https://fonts.googleapis.com/css2?family=Bebas+Neue&family=Roboto:wght@400&display=swap" rel="stylesheet">
<style>
  :root {
    --page: #ffffff;
    --blue-deep: #0a3f8f;
    --blue-mid: #0f64c4;
    --blue-bright: #1f8fe0;
    --navy-text: #0b2e66;
    --orange: #f28c00;
    --white: #ffffff;
    --caption: #333333;
  }
  html, body {
    margin: 0;
    padding: 0;
    width: 1200px;
    height: 343px;
    overflow: hidden;
    background: var(--page);
  }
  .stage {
    position: relative;
    width: 1200px;
    height: 343px;
  }
  .banner {
    position: absolute;
    left: 171px;
    top: 56px;
    width: 857px;
    height: 171px;
    overflow: hidden;
    box-shadow: 6px 7px 8px rgba(0,0,0,0.45);
    font-family: "Bebas Neue", "Arial Narrow", sans-serif;
  }
  .banner-backdrop {
    position: absolute;
    inset: 0;
    background:
      linear-gradient(135deg, rgba(255,255,255,0.08) 0 18%, transparent 18% 30%, rgba(255,255,255,0.06) 30% 44%, transparent 44%),
      linear-gradient(100deg, var(--blue-mid) 0%, var(--blue-bright) 30%, var(--blue-mid) 55%, var(--blue-deep) 100%);
  }
  .logo-spot {
    position: absolute;
    left: 36px;
    top: 0;
    width: 162px;
    height: 162px;
    border-radius: 50%;
    background: var(--orange);
    display: flex;
    align-items: center;
    justify-content: center;
    color: var(--white);
    font-size: 44px;
    letter-spacing: 20px;
    padding-left: 20px;
    box-sizing: border-box;
  }
  .event-title {
    position: absolute;
    left: 201px;
    top: 2px;
    width: 628px;
    margin: 0;
    color: var(--white);
    font-weight: 400;
    font-size: 55px;
    line-height: 52px;
    display: flex;
    justify-content: space-between;
  }
  .tab {
    position: absolute;
    background: var(--orange);
    border-radius: 6px;
    text-align: center;
    box-sizing: border-box;
  }
  .fest-name {
    left: 298px; top: 51px; width: 122px; height: 29px;
    color: var(--white); font-size: 25px; line-height: 30px;
  }
  .fest-time {
    left: 274px; top: 76px; width: 168px; height: 40px;
    color: var(--navy-text); font-size: 26px; line-height: 42px;
  }
  .fest-details {
    left: 219px; top: 116px; width: 280px; height: 60px;
    color: var(--navy-text); font-size: 11.5px; line-height: 14.5px;
    padding-top: 5px;
  }
  .price {
    position: absolute;
    color: var(--white);
    font-size: 31px;
    line-height: 30px;
  }
  .price-session { left: 518px; top: 63px; }
  .price-kids { left: 531px; top: 99px; }
  .price-note {
    left: 563px; height: 29px;
    color: var(--white); font-size: 18px; line-height: 30px;
    text-align: left; padding-left: 6px;
  }
  .note-session { top: 61px; width: 257px; }
  .note-kids { top: 97px; width: 178px; }
  .fine-print {
    position: absolute;
    color: var(--white);
    margin: 0;
  }
  .kids-extra { left: 569px; top: 128px; font-size: 16px; line-height: 16px; }
  .exception { left: 528px; top: 152px; font-size: 12.5px; line-height: 14px; }
  .size-caption {
    position: absolute;
    left: 0;
    width: 1200px;
    top: 264px;
    text-align: center;
    font-family: "Roboto", Arial, sans-serif;
    font-size: 28px;
    color: var(--caption);
  }
</style>
</head>
<body>
<div class="stage">
  <section class="banner">
    <div class="banner-backdrop" role="img" aria-label="Event background artwork in blue tones with diagonal light stripes"></div>
    <div class="logo-spot">LOGO</div>
    <h1 class="event-title"><span>S</span><span>P</span><span>R</span><span>I</span><span>N</span><span>G</span><span>&nbsp;</span><span>F</span><span>R</span><span>E</span><span>N</span><span>Z</span><span>Y</span></h1>

    <div class="tab fest-name">Field Jubilee</div>
    <div class="tab fest-time">9:00 AM - 12:00 PM</div>
    <div class="tab fest-details">Include our annual Hoop Hustle event at 11:00 AM, where children ages 3-12 receive a free t-shirt, free basketball, and two free tickets to the men’s semi-final games</div>

    <div class="price price-session">$15</div>
    <div class="tab price-note note-session">Each session consists of two games</div>
    <div class="price price-kids">$5</div>
    <div class="tab price-note note-kids">Kids tickets per session</div>
    <p class="fine-print kids-extra">Include a hot dog and drink</p>
    <p class="fine-print exception">The exception of the championship games on Sunday, March 12</p>
  </section>
  <div class="size-caption">1000px x 200px</div>
</div>
</body>
</html>
```